The most modern business card ever !!!

Our company call “Tavlin”. Tavlin is a technology company specialized in cruises solutions. Out main product is a platform to reserve cruises. This is a revolutionary platform that make easier to travel agencies and final users to reserve cruises across dozen companies like brindle, pelvo, tkw, vbd, etc..We are a “start up”, with a young team of developers and we want to transmit it.. For it, we want something different, a modern business card that represent cruises and technology.. When someone receive this card, this person should say: wowww this is different… this is modern… this is a cruise related company..
Contact Information for Business Card
Requirements
Must have
- diferent, modern
Should not have
- traditions business card

```html
<!DOCTYPE html>
<html lang="en">
<head>
<meta charset="utf-8">
<title>Tavlin business card</title>
<link href="https://fonts.googleapis.com/css2?family=Roboto:wght@400;500;700&display=swap" rel="stylesheet">
<style>
  :root {
    --stage: #e9ecee;
    --brand-light: #2aaee2;
    --brand-deep: #0a8aaa;
    --ink: #111111;
    --ink-soft: #2e2e2e;
    --paper: #ffffff;
  }
  * { box-sizing: border-box; margin: 0; padding: 0; }
  html, body {
    width: 1200px; height: 1200px; overflow: hidden;
    background: var(--stage);
    font-family: "Roboto", Arial, sans-serif;
  }
  .card {
    position: absolute; top: 199px;
    width: 482px; height: 803px;
    box-shadow: 0 6px 18px rgba(0,0,0,0.18);
  }
  .card--front {
    left: 92px;
    background: radial-gradient(circle at 39% 41%, var(--brand-light) 0%, #1a9fcc 45%, var(--brand-deep) 100%);
  }
  .card--back { left: 626px; background: var(--paper); }

  .front-wordmark {
    position: absolute; left: 84px; top: 232px;
    font-size: 76px; font-weight: 500; line-height: 1;
    color: var(--paper); letter-spacing: 6px;
  }
  .site-pill {
    position: absolute; left: 65px; top: 637px;
    width: 349px; height: 48px; border-radius: 24px;
    background: var(--paper);
    display: flex; align-items: center; justify-content: center;
    font-size: 18px; font-weight: 700; letter-spacing: 2px;
    color: var(--ink-soft);
  }
  .site-pill .site-name { color: var(--brand-light); }

  .vertical {
    position: absolute;
    writing-mode: vertical-rl;
    transform: rotate(180deg);
  }
  .holder {
    left: 80px; bottom: 450px;
    line-height: 26px;
  }
  .holder__name { font-size: 20px; font-weight: 700; letter-spacing: 5.5px; color: var(--ink); }
  .holder__role { font-size: 17px; font-weight: 400; letter-spacing: 5px; color: var(--ink-soft); }

  .bars { position: absolute; left: 73px; top: 395px; width: 60px; height: 30px; }

  .back-wordmark {
    left: 264px; bottom: 378px;
    font-size: 76px; font-weight: 500; line-height: 64px;
    color: var(--ink); letter-spacing: 16px;
  }
  .brand-band {
    position: absolute; left: 346px; top: 113px;
    width: 60px; height: 312px;
    background: linear-gradient(180deg, var(--brand-deep) 0%, var(--brand-light) 50%, var(--brand-deep) 100%);
  }
  .contacts {
    position: absolute; left: 72px; top: 601px;
    list-style: none;
    font-size: 19px; font-weight: 500; letter-spacing: 2.6px;
    color: var(--ink); line-height: 41px;
  }
</style>
</head>
<body>
  <section class="card card--front">
    <div class="front-wordmark">Tavlin</div>
    <div class="site-pill">www.<span class="site-name">tavlinsite</span>.com</div>
  </section>

  <section class="card card--back">
    <div class="vertical holder">
      <div class="holder__name">Your Name Here</div>
      <div class="holder__role">Designation</div>
    </div>
    <svg class="bars" viewBox="0 0 60 30" aria-hidden="true">
      <rect x="0" y="0" width="6" height="30" fill="#111111"/>
      <rect x="12" y="0" width="48" height="10" fill="#2aaee2"/>
      <rect x="12" y="17" width="48" height="13" fill="#111111"/>
    </svg>
    <div class="vertical back-wordmark">Tavlin</div>
    <div class="brand-band"></div>
    <ul class="contacts">
      <li>- hello@tavlin.io</li>
      <li>- 555 +0192 3847 620</li>
      <li>- Harbor Lane Street 48. Etc</li>
    </ul>
  </section>
</body>
</html>
```